Restyle corporate identity (+ logo) for a road construction company

We need a new logo and stationary design for our company VORMAX path. VORMAX path® increases the road base strength, while reducing major costs and time of road construction. Attached some examples of the current design.

Our wishes for the new logo:
- Business look
- Style sheet
- Modern

More information: www.vormaxpath-example.com
Updates

Target Market(s)

Government

Industry/Entity Type

Construction

Requirements
Must have
• Logo (with road sign) + text

```html
<!DOCTYPE html>
<html lang="en">
<head>
<meta charset="utf-8">
<title>VORMAX path – Business Cards</title>
<link rel="stylesheet" href="https://fonts.googleapis.com/css2?family=Cabin+Condensed:wght@400;500&display=swap">
<style>
  :root {
    --lime: #a9cf38;
    --white: #ffffff;
    --ink: #3f4442;
    --grey: #7d8082;
    --backdrop: #6d6e72;
    --card-shadow: rgba(0, 0, 0, 0.35);
  }
  * { box-sizing: border-box; margin: 0; padding: 0; }
  html, body {
    width: 1200px;
    height: 1000px;
    overflow: hidden;
  }
  body {
    background: var(--backdrop);
    font-family: "Cabin Condensed", "Arial Narrow", sans-serif;
    display: flex;
    align-items: center;
    justify-content: center;
    gap: 40px;
  }
  .card {
    position: relative;
    width: 540px;
    height: 350px;
    overflow: hidden;
    box-shadow: 0 14px 30px var(--card-shadow);
  }

  /* Front */
  .card--front {
    background: var(--lime);
    display: flex;
    align-items: center;
    justify-content: center;
  }
  .brand {
    display: flex;
    align-items: center;
    gap: 18px;
    font-weight: 400;
    white-space: nowrap;
  }
  .brand__dot {
    border-radius: 50%;
    flex: none;
  }
  .card--front .brand { color: var(--white); font-size: 64px; letter-spacing: 1px; }
  .card--front .brand__dot { width: 84px; height: 84px; background: var(--white); }
  .brand sup { font-size: 0.3em; vertical-align: top; }

  /* Back */
  .card--back { background: var(--white); }
  .back__band {
    position: absolute;
    inset: 0;
    width: 100%;
    height: 100%;
  }
  .back__band polygon { fill: var(--lime); }
  .card--back .brand {
    position: absolute;
    left: 30px;
    bottom: 34px;
    color: var(--grey);
    font-size: 40px;
    gap: 12px;
  }
  .card--back .brand__dot { width: 48px; height: 48px; background: var(--lime); }

  .contact {
    position: absolute;
    top: 30px;
    right: 34px;
    text-align: right;
    line-height: 1.25;
  }
  .contact__name { color: var(--white); font-size: 30px; font-weight: 500; }
  .contact__role { color: var(--ink); font-size: 18px; margin-top: 6px; }
  .contact__lines { color: var(--white); font-size: 16px; margin-top: 18px; }
  .contact__address { color: var(--ink); font-size: 16px; margin-top: 14px; }
</style>
</head>
<body>
  <section class="card card--front" aria-label="Business card front">
    <div class="brand">
      <span class="brand__dot"></span>
      <span class="brand__name">VORMAX path<sup>®</sup></span>
    </div>
  </section>

  <section class="card card--back" aria-label="Business card back">
    <svg class="back__band" viewBox="0 0 540 350" preserveAspectRatio="none" aria-hidden="true">
      <polygon points="0,0 540,0 540,350 0,120"/>
    </svg>
    <div class="contact">
      <p class="contact__name">Lena Marsh</p>
      <p class="contact__role">Member of the Board<br>Chief Executive Officer</p>
      <p class="contact__lines">
        Tel: +12 987 65 43<br>
        Email: lena@vormaxpath-example.com<br>
        Site: www.vormaxpath-example.com
      </p>
      <p class="contact__address">
        Kanaalweg 58<br>
        4021 BM Rivenstad<br>
        The Netherlands
      </p>
    </div>
    <div class="brand">
      <span class="brand__dot"></span>
      <span class="brand__name">VORMAX path<sup>®</sup></span>
    </div>
  </section>
</body>
</html>
```